Digital Menu for New Picnic Company

We're in the process of creating a new picnic business called Cedar Hollow Hampers. We need our menu created as per the content in this google doc https://files.examplecloud.net/doc/7Kq2Rv9LmTzX4bWcYhJnPaE3sUd8FgVoNiQ5rMtLyKe/view?share=link
Please look at our website www.cedarhollowhampers.com.au to get an understanding of what we do and our branding style. We need the menu to be created matching the branding/colours as per our website however other than that please feel free to design it however you like and I will provide feedback from there. We are offering a high end gourmet product so the look and feel of the menu does need to reflect this.
PLEASE NOTE: This menu will only be displayed online as a PDF and doesn't need to be printed or provided physically.

```html
<!DOCTYPE html>
<html lang="en">
<head>
<meta charset="utf-8">
<title>Cedar Hollow Hampers – Gourmet Picnic Menu</title>
<link href="https://fonts.googleapis.com/css2?family=Montserrat:wght@400;500;700&family=Great+Vibes&display=swap" rel="stylesheet">
<style>
:root{
  --mint:#cfeadb;
  --sky:#4fc3f0;
  --band:#0aa6e6;
  --leaf:#6cbe45;
  --script:#5cb531;
  --ink:#1e1e1e;
  --dot:#e23b3b;
  --white:#ffffff;
}
*{box-sizing:border-box;margin:0;padding:0}
html,body{width:1000px;height:1200px;overflow:hidden;background:var(--mint)}
body{position:relative;font-family:'Montserrat',sans-serif;color:var(--ink)}
.page{position:absolute;width:365px;height:513px;box-shadow:0 2px 6px rgba(0,0,0,.18);overflow:hidden}
.page--cover{left:101px;top:68px;background:var(--leaf)}
.page--cheese{left:531px;top:68px;background:var(--sky)}
.page--crackers{left:101px;top:636px;background:var(--sky)}
.page--drinks{left:531px;top:636px;background:var(--sky)}
.sheet{position:absolute;left:18px;top:20px;width:329px;height:472px;background:var(--white)}
.cover-photo{position:absolute;left:0;top:0;width:365px;height:139px;background:linear-gradient(160deg,#2f4a26 0%,#5f7a3f 40%,#8a6b48 65%,#c9565a 85%,#e9d9d9 100%)}
.cover-band{position:absolute;left:0;top:139px;width:365px;height:92px;background:var(--band)}
.brand-name{position:absolute;left:0;width:100%;text-align:center;font-weight:700;font-size:12px;color:var(--white);letter-spacing:.3px}
.cover-title{position:absolute;left:0;top:166px;width:100%;text-align:center;font-weight:700;font-size:24px;color:var(--white)}
.cover-menu{position:absolute;left:0;top:196px;width:100%;text-align:center;font-family:'Great Vibes',cursive;font-size:32px;color:var(--white);line-height:1}
.intro-card{position:absolute;left:30px;top:231px;width:306px;height:242px;background:var(--white)}
.intro-text{position:absolute;left:10px;top:21px;width:286px;z-index:2}
.intro-text p{font-size:6.7px;line-height:10.6px;text-align:center;margin-bottom:10.6px;letter-spacing:-.05px}
.intro-text p:last-child{margin-bottom:0}
.badge{position:absolute;left:17px;top:440px;width:58px;height:58px;border-radius:50%;background:var(--band)}
.tablecloth{position:absolute;left:199px;top:429px}
.script-title{position:absolute;left:0;width:100%;text-align:center;font-family:'Great Vibes',cursive;color:var(--script);font-size:36px;line-height:1}
.rule{position:absolute;left:18px;width:292px;display:flex;align-items:center;font-size:10.5px;letter-spacing:.3px}
.rule::before,.rule::after{content:"";flex:1;height:1px;background:var(--ink)}
.rule span{padding:0 10px}
.section-head{position:absolute;font-weight:700;font-size:10.5px;line-height:12.5px}
.list{position:absolute;list-style:none;font-size:7.4px;line-height:13.7px}
.list li{position:relative;padding-left:8px}
.list li::before{content:"";position:absolute;left:0;top:4.5px;width:4px;height:4px;border:1px solid var(--dot);border-radius:50%}
.list li.cont::before{display:none}
.footer-brand{position:absolute;left:0;width:100%;text-align:center;font-weight:700;font-size:10px;color:var(--script)}
</style>
</head>
<body>

<section class="page page--cover">
  <div class="cover-photo" role="img" aria-label="Photo of a wicker picnic basket on a red gingham table in a forest clearing"></div>
  <div class="cover-band"></div>
  <div class="brand-name" style="top:145px">Cedar Hollow Hampers</div>
  <h1 class="cover-title">Gourmet Picnic</h1>
  <div class="cover-menu">• Menu •</div>
  <div class="intro-card">
    <div class="intro-text">
      <p>Our Gourmet Picnics are handcrafted and delivered to your picnic spot on a wooden grazing board. The board is sealed inside a catering box to provide peace of mind that your food hasn't been tampered with while waiting for you at the picnic spot.</p>
      <p>Once you arrive, you then open the box and remove the grazing board to begin enjoying the food. We prepare our food in accordance with food handling guidelines and all COVID-19 precautions.</p>
      <p>We also provide complimentary beverages as part of the Gourmet Picnic being your choice of beers, wine or soft drink. You also can choose between still or sparkling water. Beverages are served cold with quality glassware.</p>
      <p>As everyone has varying tastes, we have created our menu to be fully customisable so you can design your own picnic. We offer a wide variety of choices while focussing on quality ingredients for each component of your picnic. This also creates a great excuse to come back for another picnic so you can try out more of the menu.</p>
    </div>
  </div>
  <div class="badge"></div>
  <svg class="tablecloth" width="166" height="84" viewBox="0 0 166 84" role="img" aria-label="Red gingham tablecloth with white heart plates and cutlery">
    <polygon points="0,50 158,0 166,12 166,84 8,84" fill="#e0545a"/>
  </svg>
</section>

<section class="page page--cheese">
  <div class="sheet">
    <h2 class="script-title" style="top:16px">Cheese &amp; Dips</h2>
    <div class="rule" style="top:58px"><span>CHOOSE ANY 2</span></div>
    <div class="section-head" style="left:37px;top:88px">CHEESES</div>
    <ul class="list" style="left:37px;top:103px">
      <li>Creamy Blue</li><li>Blue Vein</li><li>Chilli Cream</li><li>Double Cream Brie</li><li>Camembert</li>
    </ul>
    <ul class="list" style="left:179px;top:103px">
      <li>Cheddar</li><li>Vintage Cheddar</li><li>Parmesan</li><li>Dutch Smoked</li><li>Goat Milk</li>
    </ul>
    <div class="section-head" style="left:37px;top:194px">DIPS</div>
    <ul class="list" style="left:37px;top:208px">
      <li>Mild Salsa</li><li>Spicy Salsa</li><li>Zesty Avo &amp; Feta</li><li>Roasted Garlic Hommus</li><li>Sweet Potato &amp; Cashew</li><li>Roast Pumpkin, Caramelised</li><li class="cont">Onion &amp; Cashews</li>
    </ul>
    <ul class="list" style="left:179px;top:208px">
      <li>Roasted Red Capsicum,</li><li class="cont">Cashews &amp; Basil</li><li>Basil, Pesto &amp; Cashews</li><li>Sweet Chilli &amp; Sour Cream</li><li class="cont">Caviar</li><li>Guacamole</li><li>Caramalised French Onion</li><li>Cheesy Jalapeno</li>
    </ul>
    <div class="footer-brand" style="top:448px">Cedar Hollow Hampers</div>
  </div>
</section>

<section class="page page--crackers">
  <div class="sheet" style="top:21px">
    <h2 class="script-title" style="top:16px">Crackers</h2>
    <div class="rule" style="top:57px"><span>CHOOSE ANY 2</span></div>
    <ul class="list" style="left:19px;top:80px">
      <li>Golden Rounds</li><li>Natural Artisan Crackers</li><li>Wheat Squares</li><li>Flat bread</li><li>Chilli jam flat bread</li><li>Assorted crackers</li>
    </ul>
    <ul class="list" style="left:132px;top:80px">
      <li>Veggie crackers</li><li>Pita Crackers</li><li>Bread Sticks</li><li>Corn Chips</li><li>Bruschetta Toasts</li><li>Wafer Crackers</li>
    </ul>
    <ul class="list" style="left:232px;top:80px">
      <li>Rice crackers</li><li>Rye Crispbread</li><li>Gluten free crackers</li><li>Seaweed crackers</li>
    </ul>
    <h2 class="script-title" style="top:187px">Fruit</h2>
    <div class="rule" style="top:227px"><span>CHOOSE ANY 3</span></div>
    <ul class="list" style="left:19px;top:250px">
      <li>Strawberrys</li><li>Grapes</li>
    </ul>
    <ul class="list" style="left:132px;top:250px">
      <li>Passion Fruit</li><li>Oranges</li>
    </ul>
    <ul class="list" style="left:232px;top:250px">
      <li>Kiwi Fruit</li>
    </ul>
    <h2 class="script-title" style="top:304px">Chocolates</h2>
    <div class="rule" style="top:344px"><span>CHOOSE ANY 1</span></div>
    <ul class="list" style="left:19px;top:367px">
      <li>Hazel Pralines</li><li>Alpine Nougat</li><li>Silk Truffles</li>
    </ul>
    <ul class="list" style="left:132px;top:367px">
      <li>Rocky Road</li><li>Wafer Fingers</li><li>Malt Balls</li>
    </ul>
    <ul class="list" style="left:232px;top:367px">
      <li>Milk Chocolate</li><li>Vegan/Gluten Free</li><li>Chocolate or Lolly</li>
    </ul>
    <div class="footer-brand" style="top:448px">Cedar Hollow Hampers</div>
  </div>
</section>

<section class="page page--drinks">
  <div class="sheet" style="top:21px">
    <h2 class="script-title" style="top:18px">Complimentary Beverages</h2>
    <div class="rule" style="top:58px"><span>CHOOSE ANY 2</span></div>
    <div class="section-head" style="left:25px;top:85px">WINE</div>
    <ul class="list" style="left:25px;top:100px">
      <li>Champagne</li><li>Sauvignon Blanc</li><li>Chadonnay</li><li>Malbec</li><li>Shiraz</li><li>Cabernet</li><li>Sauvignon</li><li>Merlot</li>
    </ul>
    <div class="section-head" style="left:125px;top:85px">BEER</div>
    <ul class="list" style="left:125px;top:100px">
      <li>Craft Lager</li><li>Craft Pale Ale</li><li>Craft XPA</li><li>Australian Lager</li><li>Australian Dry</li><li>International</li><li>Lager</li><li>Cider</li>
    </ul>
    <div class="section-head" style="left:222px;top:85px">WATER<br>PREFERENCE</div>
    <ul class="list" style="left:222px;top:114px">
      <li>Still</li><li>Sparkling</li><li>Still &amp; Sparkling</li>
    </ul>
    <div class="section-head" style="left:25px;top:234px">NON ALCOHOLIC</div>
    <ul class="list" style="left:25px;top:250px">
      <li>Classic Cola</li><li>Cola No Sugar</li><li>Diet Cola</li><li>Cola Caffeine Free</li><li>Vanilla Cola</li><li>Brisk Cola</li><li>Brisk Max</li><li>Brisk Max Vanilla</li><li>Zest Lemon Lime</li><li>Sunburst Orange</li><li>Summit Citrus</li>
    </ul>
    <ul class="list" style="left:167px;top:250px">
      <li>Lemon Squash</li><li>Lemon Squash Zero</li><li>Orange Fizz</li><li>Orange Fizz Zero</li><li>Apple Cider</li><li>Ginger Beer</li><li>Diet Ginger Beer</li><li>Lemon Lime &amp; Bitters</li><li>Creaming Soda</li><li>Sugar Free Creaming Soda</li>
    </ul>
    <div class="footer-brand" style="top:448px">Cedar Hollow Hampers</div>
  </div>
</section>

</body>
</html>
```